Conference Header for use in marketing and on website

I need a header designed that promotes an event we will be holding to be used on marketing and website. I have attached a brief with the information that needs to be on it including the colours required. It will need to include an image of Melbourne at least and our logo. If you find a better Melbourne image you wish to use, I can purchase it off Quillmark Images.

I want it to be eyecatching and exciting and vibrant while still providing the details clearly. I also want source files included.

```html
<!DOCTYPE html>
<html lang="en">
<head>
<meta charset="utf-8">
<title>Kestrel Rotoform – Rotomould Conference &amp; Exhibition 2022 Header</title>
<link rel="stylesheet" href="https://fonts.googleapis.com/css2?family=Arimo:ital,wght@0,400;0,700;1,400&display=swap">
<style>
  :root {
    --white: #ffffff;
    --slate: #6a7272;
    --ink: #111111;
    --cyan: #5fe3ef;
    --violet: #5b1ee6;
    --night-1: #2a2470;
    --night-2: #5a48b8;
    --sky: #7fb6e8;
    --gold: #b98a3c;
    --year: rgba(255, 255, 255, 0.32);
  }
  * { margin: 0; padding: 0; box-sizing: border-box; }
  html, body { width: 1200px; height: 542px; overflow: hidden; background: var(--white); }
  .header {
    position: relative;
    width: 1200px;
    height: 542px;
    overflow: hidden;
    font-family: "Arimo", Arial, sans-serif;
  }
  .backdrop { position: absolute; inset: 0; }
  .city-photo {
    position: absolute;
    left: 347px; top: 80px;
    width: 316px; height: 385px;
    background: linear-gradient(180deg, var(--sky) 0%, #a9c7dd 45%, #6d7a5c 70%, var(--gold) 88%, #3b2b1c 100%);
  }
  .event-year {
    position: absolute;
    left: 641px; top: 271px;
    transform: translate(-50%, -50%) rotate(-90deg);
    font-size: 176px;
    font-weight: 700;
    letter-spacing: 14px;
    color: var(--year);
    line-height: 1;
    white-space: nowrap;
  }
  .brand {
    position: absolute;
    left: 22px; top: 36px;
    display: flex; align-items: center; gap: 10px;
  }
  .brand-mark {
    width: 22px; height: 22px;
    background: var(--slate);
  }
  .brand-name {
    font-size: 26px;
    font-weight: 700;
    color: var(--slate);
  }
  .event-title {
    position: absolute;
    left: 18px; top: 116px;
    font-size: 43px;
    font-weight: 700;
    line-height: 58px;
    color: var(--slate);
  }
  .event-location {
    position: absolute;
    left: 18px; top: 297px;
    font-size: 23px;
    letter-spacing: 2.6px;
    color: var(--ink);
  }
  .event-dates {
    position: absolute;
    left: 18px; top: 395px;
    font-size: 21px;
    font-weight: 700;
    letter-spacing: 3px;
    color: var(--violet);
  }
  .tagline {
    position: absolute;
    left: 712px; top: 260px;
    font-size: 23px;
    font-style: italic;
    letter-spacing: 3.6px;
    color: var(--white);
    white-space: nowrap;
  }
</style>
</head>
<body>
<header class="header">
  <svg class="backdrop" width="1200" height="542" viewBox="0 0 1200 542">
    <defs>
      <linearGradient id="eventPhotoTone" x1="0" y1="0" x2="1" y2="1">
        <stop offset="0" stop-color="#5a48b8"/>
        <stop offset="0.55" stop-color="#43369a"/>
        <stop offset="1" stop-color="#2a2470"/>
      </linearGradient>
    </defs>
    <rect class="slate-field" width="1200" height="542" fill="#6a7272"/>
    <path class="cyan-arc-right" d="M600 0 C420 90 390 420 505 542 L1200 542 L1200 0 Z" fill="#5fe3ef"/>
    <path class="event-photo" role="img" aria-label="Photo of conference delegates networking at banquet tables, tinted violet"
          d="M622 0 C442 90 412 420 527 542 L1200 542 L1200 0 Z" fill="url(#eventPhotoTone)"/>
    <ellipse class="cyan-arc-left" cx="140" cy="272" rx="330" ry="392" fill="#5fe3ef"/>
    <ellipse class="white-field" cx="130" cy="272" rx="305" ry="372" fill="#ffffff"/>
  </svg>

  <div class="city-photo" role="img" aria-label="Photo of the Melbourne skyline and a bridge over the river at golden hour"></div>

  <div class="event-year">2022</div>

  <div class="brand">
    <span class="brand-mark"></span>
    <span class="brand-name">Kestrel Rotoform</span>
  </div>

  <h1 class="event-title">Rotomould<br>Conference &amp;<br>Exhibition</h1>
  <p class="event-location">Melbourne, Australia</p>
  <p class="event-dates">18 – 20 September</p>
  <p class="tagline">Reconnect with Relevance</p>
</header>
</body>
</html>
```